Website redesign

We need a bold revamp of our website (http://www.brantocksparkworks.co.nz/)
which at the moment looks dated. We want a crisp, fresh and bold look. The background image behind web page can go. Open to complete new layout

Target Market(s)

Electrical contracting company- working in the domestic and commercial field

Coding

Coded - Design and coding required

Number of Pages Required

5+ page

Font styles to use
Sans Serif

Colors

Designer to choose colors to be used in the design.

```html
<!DOCTYPE html>
<html lang="en">
<head>
<meta charset="utf-8">
<title>Brantock Sparkworks – Electrical services</title>
<link href="https://fonts.googleapis.com/css2?family=Lato:wght@400;700&display=swap" rel="stylesheet">
<style>
:root{
  --accent:#4049ff;
  --ink:#1a1a1a;
  --nav:#333;
  --muted:#9aa0a8;
  --rule:#ececec;
  --white:#fff;
}
*{margin:0;padding:0;box-sizing:border-box}
html,body{width:1200px;height:1060px;overflow:hidden;background:var(--white);font-family:'Lato',sans-serif;color:var(--ink)}
.site-header{position:relative;height:88px}
.brand{position:absolute;left:119px;top:30px;display:flex;align-items:center;gap:8px;font-weight:700;font-size:17px;color:var(--ink);line-height:1.1;width:110px}
.brand-mark{width:12px;height:12px;background:#e3161b;flex:none}
.main-nav{position:absolute;left:284px;top:36px;display:flex;gap:25px}
.main-nav a{font-size:13.5px;color:var(--nav);text-decoration:none;letter-spacing:.2px}
.header-phone{position:absolute;right:121px;top:33px;display:flex;align-items:center;gap:10px;font-weight:700;font-size:18px;color:var(--nav)}
.hero{position:relative;height:445px;overflow:hidden}
.hero-photo{position:absolute;inset:0;background:linear-gradient(100deg,#3a4150 0%,#4d5563 40%,#7b7f86 65%,#5f6570 100%)}
.hero-shade{position:absolute;inset:0;background:rgba(0,0,0,.25)}
.hero-content{position:absolute;left:120px;top:126px}
.hero-title{font-size:55px;font-weight:700;color:var(--white);letter-spacing:-.3px;line-height:1}
.hero-lead{margin-top:26px;font-size:16px;color:#d4d6da}
.btn{display:inline-block;margin-top:29px;width:141px;height:44px;line-height:44px;text-align:center;background:var(--accent);color:var(--white);font-weight:700;font-size:13.5px;border-radius:2px;text-decoration:none}
.about{position:relative;height:527px}
.about-photo{position:absolute;left:202px;top:99px;width:387px;height:349px;background:linear-gradient(135deg,#d9dde2 0%,#6f8fa8 45%,#2a5f92 70%,#c9ced4 100%)}
.about-text{position:absolute;left:611px;top:165px;width:370px}
.about-text::before{content:"";display:block;width:37px;height:3px;background:var(--accent);margin-bottom:6px}
.about-title{font-size:35px;font-weight:400;color:#111}
.about-text p{margin-top:15px;font-size:13.5px;line-height:21px;color:var(--muted)}
.about-text p + p{margin-top:0}
.divider{position:absolute;left:119px;right:121px;top:1034px;height:1px;background:var(--rule)}
</style>
</head>
<body>
<header class="site-header">
  <div class="brand"><span class="brand-mark"></span>Brantock Sparkworks</div>
  <nav class="main-nav">
    <a href="#">HOME</a><a href="#">ABOUT US</a><a href="#">SERVICES</a><a href="#">PROJECTS</a><a href="#">CONTACT US</a>
  </nav>
  <div class="header-phone">
    <svg width="15" height="18" viewBox="0 0 24 24"><path fill="#333" d="M6.6 2.5l3 3.6c.4.5.4 1.2 0 1.7L8 9.6c1.2 2.6 3.5 5 6.3 6.4l1.8-1.6c.5-.4 1.2-.5 1.7-.1l3.6 2.8c.5.4.6 1.1.3 1.6l-1.6 2.6c-.4.6-1.1.9-1.8.8C9.8 21 3 14.2 2.1 5.7c-.1-.7.2-1.4.8-1.8L5 2.3c.5-.3 1.2-.3 1.6.2z"/></svg>
    0800 55 41 27
  </div>
</header>

<section class="hero">
  <div class="hero-photo" role="img" aria-label="Electrician in cap working on a wired switchboard"></div>
  <div class="hero-shade"></div>
  <div class="hero-content">
    <h1 class="hero-title">Electrical services</h1>
    <p class="hero-lead">Lorem ipsum dolor sit amet, consectetur adipiscing elit, sed do eiusmod tempor.</p>
    <a class="btn" href="#">Contact us</a>
  </div>
</section>

<section class="about">
  <div class="about-photo" role="img" aria-label="Close-up of a switchboard with coloured wiring and circuit breakers"></div>
  <div class="about-text">
    <h2 class="about-title">About</h2>
    <p>Brantock Sparkworks is a leading electrical installation and maintenance company based in Wanganui, but servicing all New Zealand.</p>
    <p>With over 15 professionally qualified and experienced Wanganui electricians, technicians and support staff we are leading the way in providing quality electrical services.</p>
  </div>
</section>
<div class="divider"></div>
</body>
</html>
```